International Energy Consultancy requires a "Company Capabilities Statement" in the for...

We need a capability statement polished, using the design and words provided. I have included a mockup/draft for reference. I have also added in our Company LogoWhat I would like at the end this, is to be able to tailor it depending on which client etc we are sending it to, for example change the text, case study and photograph etc).By way of background, Corvanta Partners is an expert team consultants with skills across the energy sector. https://corvantapartners.example/

Colors

Designer to choose colors to be used in the design.

Requirements
Must have
• View ppt provided to see what content is requires

```html
<!DOCTYPE html>
<html lang="en">
<head>
<meta charset="utf-8">
<title>Corvanta Partners – Capabilities Statement</title>
<link rel="stylesheet" href="https://fonts.googleapis.com/css2?family=Source+Sans+3:wght@400;600;700&display=swap">
<style>
:root{
  --page:#e9e9e9;
  --navy:#1f3566;
  --blue:#1a7fc4;
  --blue-light:#2aa6e0;
  --blue-dark:#0b4f8f;
  --panel-light:#eef0f2;
  --panel-dark:#3b3b3e;
  --ink:#3a3a3a;
  --white:#ffffff;
}
*{box-sizing:border-box;margin:0;padding:0}
html,body{width:1200px;height:954px;overflow:hidden;background:var(--page)}
body{font-family:"Source Sans 3",Arial,sans-serif;color:var(--ink)}
.sheet-frame{position:absolute;left:30px;top:73px;width:1140px;height:807px;box-shadow:0 4px 14px rgba(0,0,0,.25)}
.sheet{position:absolute;left:0;top:0;width:840px;height:595px;transform:scale(1.3572);transform-origin:0 0;background:var(--white);overflow:hidden}

/* header */
.masthead{position:absolute;left:0;top:0;width:840px;height:115px;background:linear-gradient(180deg,#2d4a82 0%,#243c70 45%,#1a2f5e 100%)}
.masthead-scene{position:absolute;left:0;top:0;width:520px;height:115px;background:linear-gradient(90deg,rgba(70,110,160,.55),rgba(40,70,120,.25) 70%,rgba(0,0,0,0))}
.headline{position:absolute;left:12px;top:18px;width:300px;color:var(--white);font-size:16.5px;line-height:22px;font-weight:400}
.brand{position:absolute;left:560px;top:38px;display:flex;align-items:center;gap:10px;color:var(--white);font-size:27px;font-weight:600;letter-spacing:.2px}
.brand-mark{width:30px;height:30px;border-radius:50%;background:var(--white)}

/* columns */
.col-left{position:absolute;left:0;top:115px;width:295px;height:445px;background:var(--panel-light)}
.col-mid{position:absolute;left:295px;top:115px;width:250px;height:445px;background:var(--panel-dark);color:var(--white)}
.col-right{position:absolute;left:545px;top:115px;width:295px;height:445px;background:var(--white)}

.tab{position:absolute;height:15px;padding:0 8px;line-height:15px;font-size:8px;font-weight:700;color:var(--white);text-transform:uppercase;background:linear-gradient(90deg,var(--blue-light),var(--blue));border-top-right-radius:4px}

.map{position:absolute;left:0;top:15px;width:295px;height:153px;background:radial-gradient(ellipse at 55% 45%,#9a9c9f 0%,#c4c6c9 45%,#e2e3e5 80%)}
.photo{position:absolute;left:0;top:0;width:295px;height:167px;background:linear-gradient(180deg,#5e95d3 0%,#9cc3ea 38%,#d8dde2 52%,#2f3f63 70%,#1d2a48 100%)}

.section-title{position:absolute;font-size:9px;font-weight:700;color:var(--blue);text-transform:uppercase}

.bullets{position:absolute;list-style:none;font-size:7.2px;line-height:8.4px}
.bullets li{position:relative;padding-left:9px;margin-bottom:4.4px}
.bullets li::before{content:"";position:absolute;left:0;top:1.6px;width:4.6px;height:4.6px;border:1px solid var(--blue);border-radius:50%}
.bullets-dark li::before{border-color:var(--blue-light)}

.services{position:absolute;left:8px;top:30px;width:236px;list-style:none;font-size:7px;line-height:7.4px}
.services li{display:flex;align-items:center;gap:6px;min-height:12px;margin-bottom:4px}
.service-icon{flex:none;width:12px;height:12px;border-radius:50%;background:var(--white);position:relative}
.service-icon::after{content:"";position:absolute;left:4px;top:4px;width:4px;height:4px;border-radius:1px;background:var(--panel-dark)}

.case-intro{position:absolute;left:12px;top:195px;width:272px;font-size:7.3px;line-height:8.6px;text-align:justify}

.footer-band{position:absolute;left:0;top:560px;width:840px;height:35px;background:linear-gradient(90deg,var(--blue-light) 0%,var(--blue) 55%,var(--blue-dark) 100%)}
.site{position:absolute;left:17px;top:570px;color:var(--white);font-size:12.5px;font-weight:400}
</style>
</head>
<body>
<div class="sheet-frame">
<div class="sheet">

  <header class="masthead">
    <div class="masthead-scene" role="img" aria-label="Coastal seascape photograph with headland and surf"></div>
    <h1 class="headline">Corvanta Partners is an expert team of consultants with skills across the entire energy sector</h1>
    <div class="brand"><span class="brand-mark"></span>Corvanta Partners</div>
  </header>

  <section class="col-left">
    <div class="tab" style="left:0;top:0;width:180px">Places we’ve worked</div>
    <div class="map" role="img" aria-label="World map with pins marking project locations"></div>
    <h2 class="section-title" style="left:9px;top:181px">Key projects</h2>
    <ul class="bullets" style="left:9px;top:197px;width:278px">
      <li>Energy planning, grid integration studies, project design, ESIA, procurement and construction supervision in the Pacific. Includes projects such as 1.1 MWp PV with SCADA integrated remote control in Nauru, and 65 kWp PV, 72 kW/165 kWh BESS automated PV/battery/diesel hybrid system on Marenu Island, Palau (in progress)</li>
      <li>Atoll Power Roadmap</li>
      <li>Capacity building for Department of Grid and Power, Myanmar</li>
      <li>Project inception, feasibility studies, bidding documentation for solar and battery projects in the Caribbean</li>
      <li>Pacific Capacity Building and Training Workshops</li>
      <li>Energy sector opportunities and vision, Taranaki, New Zealand</li>
      <li>Solar Fuel-saver projects and Solar PV and grid integration projects</li>
      <li>GHG emissions and offsetting for a greenfields gas project in New Zealand</li>
    </ul>
  </section>

  <section class="col-mid">
    <div class="tab" style="left:0;top:0;width:165px">Services we provide</div>
    <ul class="services">
      <li><span class="service-icon"></span>Solar PV, solar thermal, wind, battery energy storage project expertise</li>
      <li><span class="service-icon"></span>Contract development &amp; negotiation</li>
      <li><span class="service-icon"></span>Sophisticated financial modelling</li>
      <li><span class="service-icon"></span>Strategic planning</li>
      <li><span class="service-icon"></span>Feasibility studies, project concept design &amp; specification / Owner’s Engineer and construction supervision</li>
      <li><span class="service-icon"></span>Stakeholder engagement</li>
      <li><span class="service-icon"></span>Environmental Impact Assessments (EIAs) / Environment Management Plans</li>
      <li><span class="service-icon"></span>Project management, risk management</li>
      <li><span class="service-icon"></span>Best Practice Environmental Options / Environmental Monitoring / Auditing</li>
      <li><span class="service-icon"></span>Compliance for Environmental Legislation &amp; Regulations</li>
      <li><span class="service-icon"></span>RE Training and capacity building</li>
      <li><span class="service-icon"></span>Health and Safety training and auditing</li>
    </ul>
    <div class="tab" style="left:0;top:250px;width:165px">Consultants experience</div>
    <ul class="bullets bullets-dark" style="left:9px;top:272px;width:236px">
      <li>Commercial Lead for Solara One solar thermal plant / Wind farm on Halvern Island / Northsea Array offshore opportunity</li>
      <li>Environmental and Social Safeguards for RE projects</li>
      <li>Wind Farm tender evaluations, Territory Wind Rounds I, II and III, Australia</li>
      <li>Consultancy advice for Kaurimu wind farm stages I, II and III, NZ</li>
      <li>Consultancy advice for Barrow Ridge I wind farm, Australia</li>
      <li>Technical due diligence of wind turbines</li>
    </ul>
  </section>

  <section class="col-right">
    <div class="photo" role="img" aria-label="Photograph of solar panel array in front of a power station under blue sky"></div>
    <div class="tab" style="left:0;top:167px;width:165px">Case study</div>
    <p class="case-intro">Corvanta Partners recently conducted project management, feasibility studies, environmental and social impact assessment, oversight engineering and representation services as part of the USD50 million Island Renewables Facility. We optimised project development, design &amp; delivery for:</p>
    <ul class="bullets" style="left:12px;top:252px;width:276px">
      <li>Fiji Islands - 225 kW, 153 kW &amp; 153 kW PV/diesel hybrid systems</li>
      <li>Funafuti, Tuvalu - 500 kW PV, diesel/PV control</li>
      <li>Tarawa, Kiribati – 500 kW PV, diesel/PV control</li>
      <li>Nauru – 500 kW PV</li>
      <li>Majuro, Marshall Islands – 600 kW PV</li>
      <li>Pohnpei, Micronesia – 600 kW PV</li>
      <li>Palau islands – 100 kW &amp; 100 kW PV/diesel hybrid systems &amp; water purification</li>
      <li>Aleipata, Samoa – 550 kW wind</li>
    </ul>
  </section>

  <footer class="footer-band"></footer>
  <div class="site">www.corvantapartners.example</div>

</div>
</div>
</body>
</html>
```